Business Card Design Project

We require business cards for "Venoth". We are composed of elite prior military personnel. Our goal is to provide site security for premium businesses who want on the most professional of agents on their premises. Additionally, we will provide executive protection for individuals who require professionalism, flexibility, and dedication

We want this business card to communicate professionalism, dependability, strength. However, we are not an overtly tactical agency and do not want to intimidate our clients personnel or their client. We want to give them a sense of security.
Updates

At the request of one of the designers I've listed the appropriate text that should appear on the card. Please feel free to arrange it in a creative and professional manor.

I've also uploaded a .png file of the triangle logo with no text. Please feel free to incorporate this into your designs.

ThanksĀ 

Target Market(s)

Premium businesses, executives, celebrities, and governments.

Industry/Entity Type

Security

Requirements
Must have
• Text Info that will go on the card. It does not have to be in this order:
Name
Title
Office Phone Number
Cell Phone Number
Email
Website
Mailing Address
Nice to have
• On the back I'd like to see the triangle portion of the logo displayed in a creative way that leaves enough room to write down information if needed.
Should not have
• - Weapons, Globes, or Shields. Every rent-a-cop company has that, and that's not what we are.

```html
<!DOCTYPE html>
<html lang="en">
<head>
<meta charset="utf-8">
<title>Venoth Business Card</title>
<link href="https://fonts.googleapis.com/css2?family=Ubuntu:wght@300;400;700&display=swap" rel="stylesheet">
<style>
  :root {
    --backdrop: #e9e9ea;
    --card-front: #4a4a4c;
    --card-back: #ffffff;
    --accent: #1e9ad6;
    --accent-deep: #0c5fa3;
    --text-light: #ffffff;
    --seam: #cfd3d8;
  }
  * { margin: 0; padding: 0; box-sizing: border-box; }
  html, body {
    width: 1200px; height: 448px; overflow: hidden;
    background: var(--backdrop);
    font-family: "Ubuntu", sans-serif;
  }
  .card-spread {
    position: absolute; left: 78px; top: 75px;
    width: 1040px; height: 297px;
    box-shadow: 0 4px 10px rgba(0,0,0,0.25);
    overflow: hidden;
  }
  .card-front {
    position: absolute; left: 0; top: 0; width: 523px; height: 297px;
    background: var(--card-front);
  }
  .card-back {
    position: absolute; left: 523px; top: 0; width: 517px; height: 297px;
    background: var(--card-back);
  }
  .accent-shape { position: absolute; left: 0; top: 0; }
  .brand {
    position: absolute; left: 28px; top: 26px;
    display: flex; align-items: center; gap: 12px;
    z-index: 2;
  }
  .brand-dot { width: 22px; height: 22px; border-radius: 50%; background: var(--accent); }
  .brand-name {
    color: var(--text-light); font-weight: 700; font-size: 32px; letter-spacing: 1px; line-height: 38px;
  }
  .holder { position: absolute; left: 80px; top: 114px; color: var(--text-light); z-index: 2; }
  .holder-name { font-size: 18px; font-weight: 400; line-height: 22px; }
  .holder-title { font-size: 14px; color: var(--accent); font-weight: 300; line-height: 18px; }
  .contact-list {
    position: absolute; left: 84px; list-style: none; z-index: 2;
    color: var(--text-light); font-size: 14px; font-weight: 300;
  }
  .contact-list li { display: flex; align-items: center; gap: 6px; line-height: 18px; height: 18px; white-space: nowrap; }
  .contact-list .indent { padding-left: 16px; }
  .contact-direct { top: 159px; }
  .contact-office { top: 216px; }
  .icon { width: 10px; height: 10px; flex: none; fill: var(--accent); }
  .icon-gap { margin-left: 6px; }
  .web-highlight { color: var(--accent); font-weight: 400; }
</style>
</head>
<body>
  <div class="card-spread">
    <section class="card-front"></section>
    <section class="card-back"></section>
    <svg class="accent-shape" width="1040" height="297" viewBox="0 0 1040 297" aria-hidden="true">
      <defs>
        <linearGradient id="accentFill" x1="0" y1="0" x2="1" y2="1">
          <stop offset="0" stop-color="#1e9ad6"/>
          <stop offset="1" stop-color="#0c5fa3"/>
        </linearGradient>
      </defs>
      <circle cx="600" cy="200" r="170" fill="url(#accentFill)"/>
      <line x1="523.5" y1="0" x2="523.5" y2="297" stroke="#cfd3d8" stroke-opacity="0.6"/>
    </svg>

    <div class="brand">
      <span class="brand-dot"></span>
      <span class="brand-name">VENOTH</span>
    </div>
    <div class="holder">
      <p class="holder-name">CARDHOLDER NAME</p>
      <p class="holder-title">Designation</p>
    </div>
    <ul class="contact-list contact-direct">
      <li><svg class="icon" viewBox="0 0 10 10"><path d="M3 0h4a1 1 0 0 1 1 1v8a1 1 0 0 1-1 1H3a1 1 0 0 1-1-1V1a1 1 0 0 1 1-1zm0.2 1.2v6.6h3.6V1.2z"/></svg><span>+012 3456 7890</span></li>
      <li><svg class="icon" viewBox="0 0 10 10"><rect x="0" y="2" width="10" height="6" rx="0.5"/></svg><span>cardholder.name@venoth.com</span></li>
    </ul>
    <ul class="contact-list contact-office">
      <li><svg class="icon" viewBox="0 0 10 10"><path d="M5 0a3.5 3.5 0 0 1 3.5 3.5C8.5 6 5 10 5 10S1.5 6 1.5 3.5A3.5 3.5 0 0 1 5 0z"/></svg><span>01 Sunset Avenue, Suite No. 123,</span></li>
      <li class="indent"><span>Your City, Code, Country</span></li>
      <li><svg class="icon" viewBox="0 0 10 10"><circle cx="5" cy="5" r="5"/></svg><span>+012 345 6789</span><svg class="icon icon-gap" viewBox="0 0 10 10"><rect x="0" y="3" width="10" height="7" rx="1"/><rect x="2" y="0" width="6" height="3"/></svg><span>+012 345 6780</span></li>
      <li><svg class="icon" viewBox="0 0 10 10"><circle cx="5" cy="5" r="4.3" fill="none" stroke="#1e9ad6" stroke-width="1.2"/><path d="M0.7 5h8.6M5 0.7v8.6" stroke="#1e9ad6" stroke-width="1"/></svg><span>www.<span class="web-highlight">VENOTH</span>.com</span></li>
    </ul>
  </div>
</body>
</html>
```